UK Glass Restoration Company needs a Direct Mail Postcard Design

We need a HARD HITTING, COMPELLING 300dpi Camera Ready double sided postcard.
The dimensions will be 109mm x 152mm including bleed. We are a scratched glass repair / etched graffiti removal glass restoration company based in London, UK.
We operate mainly within the construction and commercial marketplace, however this particular postcard design is aimed solely at shop owners who have become victims of vandalism, due to etched graffiti tags and or scratches being left on their shop front glass.
We wish to focus the shop / business owners mind to the negative impact such vandalism has on the image of their business and how we are able to offer a quick and cost effective solution
We will supply text for both sides of the postcard along with relevant images, company logo and previous flyer designs, however we are happy for the selected designer to source suitable alternative images provided they are in keeping with the exact "Before" and "After" theme.
The finished postcard must preferably have a white background, but again we are open to creative suggestions.
Target Market(s)
UK SHOP OWNERS
Industry/Entity Type
It Company

```html
<!DOCTYPE html>
<html lang="en">
<head>
<meta charset="utf-8">
<title>Lucent Glass Care – Postcard</title>
<link href="https://fonts.googleapis.com/css2?family=Oswald:wght@500;700&family=Open+Sans:wght@400;600;700&display=swap" rel="stylesheet">
<style>
  :root {
    --page-bg: #e6e7e9;
    --card-white: #ffffff;
    --sky-blue: #3fb4ef;
    --deep-blue: #1b8fd6;
    --label-dark: #0d1b2a;
    --ink: #1e1e1e;
    --alert-red: #e3211d;
    --photo-warm-1: #6b4a2a;
    --photo-warm-2: #c48a4a;
    --photo-cool-1: #5d5a52;
    --photo-cool-2: #a7a295;
    --footer-grey: #f3f4f6;
  }
  * { box-sizing: border-box; margin: 0; padding: 0; }
  html, body { width: 1200px; height: 900px; overflow: hidden; }
  body {
    background: var(--page-bg);
    font-family: "Open Sans", Arial, sans-serif;
    color: var(--ink);
    position: relative;
  }
  .postcard {
    position: absolute;
    top: 62px;
    width: 555px;
    height: 775px;
    background: var(--card-white);
    overflow: hidden;
    box-shadow: 0 4px 14px rgba(0,0,0,.18);
  }
  .postcard--after { left: 35px; }
  .postcard--before { left: 612px; }

  .photo {
    position: absolute; left: 0; top: 0; width: 100%;
  }
  .postcard--after .photo {
    height: 380px;
    background: linear-gradient(160deg, var(--photo-cool-2) 0%, var(--photo-cool-1) 45%, var(--photo-warm-1) 100%);
  }
  .postcard--before .photo {
    height: 420px;
    background: linear-gradient(150deg, var(--photo-warm-2) 0%, var(--photo-warm-1) 55%, #3b2a1a 100%);
  }
  .arch { position: absolute; left: 0; width: 100%; }
  .postcard--after .arch { top: 290px; height: 120px; }
  .postcard--before .arch { top: 330px; height: 120px; }

  .state-label {
    position: absolute;
    width: 232px;
    height: 70px;
    background: var(--sky-blue);
    border-radius: 0 0 8px 8px;
    text-align: center;
    box-shadow: 0 3px 6px rgba(0,0,0,.25);
    font-family: "Oswald", "Arial Narrow", sans-serif;
  }
  .postcard--after .state-label { left: 160px; top: 270px; }
  .postcard--before .state-label { left: 166px; top: 318px; }
  .state-label__title {
    display: block; color: #fff; font-size: 27px; font-weight: 700;
    line-height: 34px; padding-top: 2px; letter-spacing: .3px;
  }
  .state-label__sub {
    display: block; color: var(--label-dark); font-size: 22px; font-weight: 500; line-height: 28px;
  }

  .pointer-arrow { position: absolute; left: 100px; top: 170px; width: 120px; height: 130px; }

  .reasons { position: absolute; left: 32px; top: 360px; width: 480px; }
  .reasons__heading {
    color: var(--alert-red); font-weight: 700; font-size: 15px; margin-bottom: 6px;
  }
  .reasons__list { list-style: none; }
  .reasons__item {
    position: relative; padding-left: 16px; font-size: 13px; line-height: 18px; margin-bottom: 3px;
  }
  .reasons__item::before {
    content: ""; position: absolute; left: 2px; top: 7px; width: 6px; height: 6px;
    border-radius: 50%; background: var(--alert-red);
  }
  .reasons__item strong { font-size: 14px; }

  .coupon {
    position: absolute; left: 50px; top: 578px; width: 456px; height: 88px;
    background: var(--sky-blue); border-radius: 12px 12px 0 0;
  }
  .coupon__badge {
    position: absolute; left: 12px; top: 12px; width: 156px; height: 56px;
    background: #fff; border: 2px solid var(--alert-red); border-radius: 16px;
    font-family: "Oswald", "Arial Narrow", sans-serif; font-weight: 700;
    font-size: 32px; line-height: 52px; text-align: center; color: var(--label-dark);
  }
  .coupon__badge span { color: var(--deep-blue); }
  .coupon__text {
    position: absolute; left: 182px; top: 6px; width: 262px;
    font-size: 12.5px; line-height: 16px; color: var(--label-dark);
  }
  .coupon__cta {
    position: absolute; left: 208px; top: 42px; color: #fff; font-size: 12.5px; font-weight: 600;
  }
  .coupon__date {
    position: absolute; left: 218px; top: 62px; width: 170px; height: 20px;
    background: #fff; border-radius: 10px;
  }

  .headline {
    position: absolute; left: 0; top: 398px; width: 100%; text-align: center;
    font-family: "Oswald", "Arial Narrow", sans-serif; font-weight: 700;
    color: var(--label-dark); font-size: 46px; line-height: 56px; text-transform: uppercase;
  }
  .headline__accent {
    color: var(--alert-red); font-style: italic; display: inline-block; transform: rotate(4deg);
  }

  .pitch {
    position: absolute; left: 30px; top: 522px; width: 500px; padding: 8px 12px;
    background: var(--sky-blue); border-radius: 14px;
    font-size: 12.5px; line-height: 17px; text-align: justify; color: var(--label-dark);
    box-shadow: 0 3px 6px rgba(0,0,0,.15);
  }
  .pitch strong { font-weight: 700; }
  .pitch .pitch__call { color: #fff; font-weight: 700; }

  .card-footer {
    position: absolute; left: 0; bottom: 0; width: 100%; height: 108px;
    background: linear-gradient(#fff, var(--footer-grey));
    border-top: 1px solid #d7d9dc;
  }
  .brand {
    position: absolute; left: 26px; top: 36px; display: flex; align-items: center; gap: 8px;
  }
  .brand__dot { width: 14px; height: 14px; border-radius: 50%; background: var(--deep-blue); }
  .brand__name { color: var(--deep-blue); font-size: 24px; font-weight: 400; }
  .contact { position: absolute; right: 26px; top: 22px; text-align: center; }
  .contact__phone {
    display: flex; align-items: center; gap: 6px; justify-content: center;
    color: var(--alert-red); font-size: 27px; font-weight: 700; line-height: 34px;
  }
  .contact__phone svg { width: 24px; height: 24px; }
  .contact__web { font-size: 18px; font-weight: 700; color: var(--ink); }
</style>
</head>
<body>

<article class="postcard postcard--after">
  <div class="photo" role="img" aria-label="Shop window with property listings behind clear, repaired glass"></div>
  <svg class="arch" viewBox="0 0 555 120" preserveAspectRatio="none">
    <path d="M0,72 Q277,0 555,60 L555,120 L0,120 Z" fill="#ffffff"/>
    <path d="M0,72 Q277,0 555,60" fill="none" stroke="#3fb4ef" stroke-width="7"/>
  </svg>
  <div class="state-label">
    <span class="state-label__title">AFTER REPAIR</span>
    <span class="state-label__sub">clear as new!</span>
  </div>

  <section class="reasons">
    <h2 class="reasons__heading">WHY LUCENT GLASS CARE?</h2>
    <ul class="reasons__list">
      <li class="reasons__item">We repair most shop window glass! We repair laminated, tempered, toughened, mirrored, tinted, and even ballistic glass.</li>
      <li class="reasons__item">We repair curved glass! Don't replace expensive curved panes – get the like-new look for less by repairing.</li>
      <li class="reasons__item">Finer work! We remove etched graffiti tags, scratches, mineral deposits, and acid etched graffiti damage .</li>
      <li class="reasons__item">Edge expertise! We can repair even deep scratches as close as 20mm from the edge of the glass.</li>
      <li class="reasons__item"><strong>Save time and money!</strong> Typical savings of up to 80% over the cost of glass replacement, with zero downtime during repair.</li>
    </ul>
  </section>

  <div class="coupon">
    <div class="coupon__badge">SAVE <span>20%</span></div>
    <p class="coupon__text">off our regular prices for scratch repair, restoration, and etched graffiti removal.</p>
    <p class="coupon__cta">ACT NOW – OFFER EXPIRES</p>
    <div class="coupon__date"></div>
  </div>

  <footer class="card-footer">
    <div class="brand"><span class="brand__dot"></span><span class="brand__name">Lucent Glass Care</span></div>
    <div class="contact">
      <div class="contact__phone">
        <svg viewBox="0 0 24 24"><path fill="#1e1e1e" d="M6.6 10.8a15.1 15.1 0 0 0 6.6 6.6l2.2-2.2c.3-.3.7-.4 1-.2 1.1.4 2.3.6 3.6.6.6 0 1 .4 1 1V20c0 .6-.4 1-1 1A17 17 0 0 1 3 4c0-.6.4-1 1-1h3.5c.6 0 1 .4 1 1 0 1.3.2 2.5.6 3.6.1.3 0 .7-.2 1z"/></svg>
        0800 555 0142
      </div>
      <div class="contact__web">www.lucentglasscare.co.uk</div>
    </div>
  </footer>
</article>

<article class="postcard postcard--before">
  <div class="photo" role="img" aria-label="Shop window with property listings behind scratched, vandalised glass"></div>
  <svg class="pointer-arrow" viewBox="0 0 120 130">
    <path d="M28,125 C10,80 30,40 72,28 L66,12 L112,30 L78,62 L74,46 C44,56 36,86 50,122 Z" fill="#e3211d" stroke="#ffffff" stroke-width="4" stroke-linejoin="round"/>
  </svg>
  <svg class="arch" viewBox="0 0 555 120" preserveAspectRatio="none">
    <path d="M0,72 Q277,0 555,60 L555,120 L0,120 Z" fill="#ffffff"/>
    <path d="M0,72 Q277,0 555,60" fill="none" stroke="#3fb4ef" stroke-width="7"/>
  </svg>
  <div class="state-label">
    <span class="state-label__title">BEFORE REPAIR</span>
    <span class="state-label__sub">A bad first impression</span>
  </div>

  <h1 class="headline">Don't let vandals<br>wreck your <span class="headline__accent">image!</span></h1>

  <p class="pitch">What's on display in your shop window? If it's graffiti, vandalism, or just wear and tear, that's the first impression your customers get – <strong>and it's not good.</strong> Lucent Glass Care remove damage from glass windows, making them sparkling clear – without replacing the glass! Our glass repair work is effective, green, and very economical. See our coupon on the other side to save even more! <span class="pitch__call">Call now for expert advice: 0800 555 0142.</span></p>

  <footer class="card-footer">
    <div class="brand"><span class="brand__dot"></span><span class="brand__name">Lucent Glass Care</span></div>
    <div class="contact">
      <div class="contact__phone">
        <svg viewBox="0 0 24 24"><path fill="#1e1e1e" d="M6.6 10.8a15.1 15.1 0 0 0 6.6 6.6l2.2-2.2c.3-.3.7-.4 1-.2 1.1.4 2.3.6 3.6.6.6 0 1 .4 1 1V20c0 .6-.4 1-1 1A17 17 0 0 1 3 4c0-.6.4-1 1-1h3.5c.6 0 1 .4 1 1 0 1.3.2 2.5.6 3.6.1.3 0 .7-.2 1z"/></svg>
        0800 555 0142
      </div>
      <div class="contact__web">www.lucentglasscare.co.uk</div>
    </div>
  </footer>
</article>

</body>
</html>
```